Automotive Accessories Business Card

Design a business template that match our new logo design and our industry.

https://www.kelvorauto.com/

Target Market(s)

Aftermarket auto parts and accessories

Industry/Entity Type

automotive

Contact Information for Business Card

company logo

Font styles to use
Serif
Sans Serif

Colors
EB3D1F
EC4F4E
F09395
F8D3D4
FCEDEE

```html
<!DOCTYPE html>
<html lang="en">
<head>
<meta charset="utf-8">
<title>Kelvor Auto – Business Card</title>
<link href="https://fonts.googleapis.com/css2?family=Montserrat:wght@400;700&display=swap" rel="stylesheet">
<style>
  :root {
    --backdrop: #9a9a9a;
    --card-white: #ffffff;
    --card-dark: #434142;
    --brand-red: #d81f27;
    --ink: #3a3839;
    --emboss: #333132;
  }
  * { box-sizing: border-box; margin: 0; padding: 0; }
  html, body {
    width: 1200px; height: 1059px; overflow: hidden;
    background: var(--backdrop);
    font-family: "Montserrat", sans-serif;
  }
  .card {
    position: absolute;
    border-radius: 24px;
  }
  .card--front {
    left: 256px; top: 89px; width: 688px; height: 391px;
    background: var(--card-white);
  }
  .card--back {
    left: 253px; top: 569px; width: 694px; height: 394px;
    background: var(--card-dark);
  }
  .brand {
    position: absolute; left: 0; right: 0;
    display: flex; align-items: center; justify-content: center; gap: 14px;
    font-weight: 700; letter-spacing: 1px;
  }
  .brand__mark { display: block; }
  .card--front .brand { top: 72px; font-size: 46px; color: var(--ink); }
  .card--front .brand__mark { width: 30px; height: 30px; background: var(--brand-red); }
  .card--back .brand { top: 158px; font-size: 70px; color: var(--emboss); }
  .card--back .brand__mark { width: 44px; height: 44px; background: var(--emboss); }
  .person {
    position: absolute; left: 0; right: 0; top: 192px; text-align: center;
  }
  .person__name {
    font-weight: 700; font-size: 27px; letter-spacing: 1px; color: var(--brand-red); line-height: 1.2;
  }
  .person__role {
    font-size: 16px; color: var(--ink); margin-top: 2px;
  }
  .address {
    position: absolute; right: 370px; top: 288px;
    text-align: right; font-size: 17px; line-height: 23px; color: var(--ink);
  }
  .divider {
    position: absolute; left: 344px; top: 278px; width: 1px; height: 68px; background: var(--ink);
  }
  .contacts {
    position: absolute; left: 372px; top: 271px; list-style: none;
    font-size: 17px; color: var(--ink); line-height: 27px;
  }
  .contacts li { display: flex; align-items: center; gap: 7px; }
  .contacts svg { width: 13px; height: 13px; fill: var(--brand-red); flex: none; }
</style>
</head>
<body>
  <section class="card card--front">
    <div class="brand"><span class="brand__mark"></span>KELVOR AUTO</div>
    <div class="person">
      <div class="person__name">DORIAN PELL</div>
      <div class="person__role">CEO/Founder</div>
    </div>
    <address class="address" style="font-style:normal">240 W. Lark Ave. Unit B<br>Fairmont, CA, 91800</address>
    <div class="divider"></div>
    <ul class="contacts">
      <li><svg viewBox="0 0 24 24"><path d="M6.6 10.8a15 15 0 0 0 6.6 6.6l2.2-2.2a1 1 0 0 1 1-.25 11.4 11.4 0 0 0 3.6.6 1 1 0 0 1 1 1V20a1 1 0 0 1-1 1A17 17 0 0 1 3 4a1 1 0 0 1 1-1h3.5a1 1 0 0 1 1 1c0 1.25.2 2.45.6 3.6a1 1 0 0 1-.25 1z"/></svg>1-866-555-0142</li>
      <li><svg viewBox="0 0 24 24"><path d="M2 5h20v2l-10 6L2 7z M2 9l10 6 10-6v10H2z"/></svg>sales@kelvorauto.com</li>
      <li><svg viewBox="0 0 24 24"><path d="M12 2a10 10 0 1 0 0 20 10 10 0 0 0 0-20zm0 2c.9 0 2.1 1.8 2.6 5H9.4C9.9 5.8 11.1 4 12 4zM4.3 10h3.1a17 17 0 0 0 0 4H4.3a8 8 0 0 1 0-4zm5.1 0h5.2a15 15 0 0 1 0 4H9.4a15 15 0 0 1 0-4zm7.2 0h3.1a8 8 0 0 1 0 4h-3.1a17 17 0 0 0 0-4zM9.4 15h5.2c-.5 3.2-1.7 5-2.6 5s-2.1-1.8-2.6-5z"/></svg>www.kelvorauto.com</li>
    </ul>
  </section>
  <section class="card card--back">
    <div class="brand"><span class="brand__mark"></span>KELVOR AUTO</div>
  </section>
</body>
</html>
```